E-commerce website for interior joinery product - Furnvale Trade

we want to create a E-commerce website to list our modular products.
other than E-commerce functions, we will also require membership logins and setting different price tiers for B2B customers (construction company and home building groups. for logos and our products etc please visit www.furnvale.co.nz
You can also get some ideas from https://brontecabinets.co.nz/ready-to-order/

Number of Pages Required

5+ page

Requirements
Must have
• on the product page, the customer can have the option to choose different colours and upgradable options.

```html
<!DOCTYPE html>
<html lang="en">
<head>
<meta charset="utf-8">
<title>Furnvale Trade – Wardrobe &amp; Door Systems</title>
<link rel="stylesheet" href="https://fonts.googleapis.com/css2?family=Merriweather:wght@400;700&family=Open+Sans:wght@400;600;700&family=Josefin+Sans:wght@700&family=Roboto+Mono:wght@400&family=Roboto:wght@500&display=swap">
<style>
:root{
  --green:#7ab648;
  --blue-btn:#1a7ff0;
  --panel-blue:#2f87bb;
  --panel-green:#21a46f;
  --grey-band:#a8a8a8;
  --cream:#f6f4ef;
  --navy:#0b1d2b;
  --ink:#333;
  --muted:#777;
  --foot:#f7f7f7;
}
*{box-sizing:border-box;margin:0;padding:0}
html,body{width:1200px;height:3487px;overflow:hidden}
body{position:relative;background:#fff;font-family:"Open Sans",sans-serif;color:var(--ink)}
.abs{position:absolute}
.serif{font-family:"Merriweather",serif}
.center{text-align:center}

/* header */
.site-header{left:0;top:0;width:1200px;height:65px;border-bottom:1px solid #eee;background:#fff}
.brand{left:208px;top:14px;display:flex;align-items:center;gap:8px;font-family:"Open Sans",sans-serif;font-size:22px;color:#6b7c86;font-weight:400}
.brand-square{width:30px;height:30px;background:#4d5d68}
.main-nav{left:650px;top:24px;display:flex;gap:22px;font-size:11px;color:#555}
.main-nav .active{color:var(--green)}
.cart{left:974px;top:20px}

/* hero */
.hero-photo{left:0;top:70px;width:1200px;height:582px;background:linear-gradient(90deg,#b9a58f 0%,#d8cfc3 35%,#e6e0d6 60%,#cfc6ba 100%)}
.hero-title{left:490px;top:312px;width:544px;height:101px;background:rgba(60,130,235,.82);color:#fff;font-family:"Roboto",sans-serif;font-weight:500;font-size:47px;line-height:101px;text-align:center}
.btn-blue{background:var(--blue-btn);color:#fff;font-family:"Roboto",sans-serif;font-weight:500;font-size:17px;border-radius:22px;display:flex;align-items:center;justify-content:center}

/* feature panels */
.panel{top:651px;width:600px;height:456px;color:#fff}
.panel-blue{left:0;background:linear-gradient(160deg,#3591c4,#2a7fb1)}
.panel-green{left:600px;background:var(--panel-green)}
.eyebrow{font-family:"Roboto Mono",monospace;font-size:10px;letter-spacing:5px}
.panel-head{font-family:"Josefin Sans",sans-serif;font-weight:700;font-size:40px;line-height:37px;letter-spacing:6px}
.panel-body{font-family:"Roboto Mono",monospace;font-size:10.5px;line-height:12.5px;letter-spacing:2.6px}

/* section titles */
.section-title{font-family:"Merriweather",serif;font-size:25px;color:#333;width:1200px;left:0;text-align:center}
.lede{font-size:11px;line-height:20px;color:#444;text-align:center}

/* products */
.product-photo{top:1189px;width:256px;height:188px}
.product-name{top:1380px;width:256px;text-align:center;font-family:"Merriweather",serif;font-size:24px;color:#333}

/* process band */
.process-band{left:0;top:1457px;width:1200px;height:394px;background:var(--grey-band)}
.col-title{font-family:"Merriweather",serif;font-size:23px;color:#222}
.step{display:flex;gap:12px;align-items:flex-start;font-family:"Merriweather",serif;font-size:13px;line-height:18px;color:#222;margin-bottom:11px}
.step svg{flex:none;margin-top:1px}

/* building */
.feature{width:260px;text-align:center}
.feature h3{font-family:"Merriweather",serif;font-size:17px;font-weight:400;color:#333;margin:18px 0 14px}
.feature p{font-size:10.5px;line-height:19.6px;color:#555}

/* best sellers */
.card{top:2514px;width:208px}
.card-photo{width:208px;height:208px;position:relative}
.sale{position:absolute;right:-4px;top:-4px;width:30px;height:30px;border-radius:50%;background:var(--green);color:#fff;font-size:9px;display:flex;align-items:center;justify-content:center}
.card-cat{font-size:9px;color:#999;margin-top:12px}
.card-name{font-family:"Merriweather",serif;font-size:12px;color:#333;margin-top:3px}
.stars{margin-top:4px;display:flex;gap:1px}
.price{font-size:10px;margin-top:4px;color:#333}
.price s{color:#999;margin-right:4px}

/* suppliers */
.suppliers{left:0;top:2832px;width:1200px;height:257px;background:var(--cream)}
.badge{width:119px;height:58px;background:#fff;display:flex;align-items:center;justify-content:center;font-family:"Open Sans",sans-serif;font-weight:600;font-size:17px;color:#444}
.badge.orange{background:#f37a1f;color:#fff}
.badge.green{background:#1d5b3a;color:#fff}

/* cta */
.cta{left:0;top:3089px;width:1200px;height:120px;background:var(--navy)}
.cta-text{left:195px;top:3134px;font-family:"Merriweather",serif;font-weight:700;font-size:25px;color:#fff}
.btn-shop{left:747px;top:3136px;width:137px;height:33px;border-radius:17px;background:var(--green);color:#fff;font-size:10px;font-weight:700;display:flex;align-items:center;justify-content:center;gap:8px;letter-spacing:.5px}

/* footer */
.site-footer{left:0;top:3209px;width:1200px;height:278px;background:var(--foot)}
.foot-head{font-size:12px;letter-spacing:2px;color:#777;font-weight:600}
.foot-link{font-size:11px;color:#444}
.foot-link.active{color:var(--green)}
.branch{font-size:11px;color:#333;line-height:19.5px}
.branch .tel{color:var(--green)}
</style>
</head>
<body>

<header class="abs site-header">
  <div class="abs brand" style="left:208px;top:15px"><span class="brand-square"></span>Furnvale</div>
  <nav class="abs main-nav">
    <span class="active">Home</span><span>Products ⌄</span><span>Gallery</span><span>Contact</span><span>Account ⌄</span>
  </nav>
  <svg class="abs cart" width="22" height="24" viewBox="0 0 22 24"><rect x="2" y="6" width="18" height="16" rx="2" fill="none" stroke="#7ab648" stroke-width="2"/><path d="M7 6V4a4 4 0 0 1 8 0v2" fill="none" stroke="#7ab648" stroke-width="2"/><text x="11" y="18" font-size="9" text-anchor="middle" fill="#7ab648" font-family="Open Sans">0</text></svg>
</header>

<div class="abs hero-photo" role="img" aria-label="Photo of a smiling consultant in a suit standing beside a light timber wardrobe with shelving"></div>
<div class="abs hero-title">New Showroom opening</div>
<div class="abs btn-blue" style="left:548px;top:432px;width:188px;height:40px">View All Products</div>
<div class="abs btn-blue" style="left:751px;top:426px;width:222px;height:39px">View new showrooms</div>

<section class="abs panel panel-blue">
  <div class="abs eyebrow" style="left:70px;top:73px">WHAT WE DO</div>
  <div class="abs panel-head" style="left:70px;top:138px;width:500px">A New Home. A Fresh Renovation.</div>
  <p class="abs panel-body" style="left:81px;top:268px;width:450px">The Furnvale offers a wide selection of sliding doors, stand-alone wardrobes, walk-in wardrobes, interior shelves, and sliding drawer constructions.</p>
</section>
<section class="abs panel panel-green">
  <div class="abs eyebrow" style="left:70px;top:67px">HOW WE WORK</div>
  <div class="abs panel-head" style="left:70px;top:133px;width:470px">Giving Your Home The New Fresh Look.</div>
  <p class="abs panel-body" style="left:81px;top:261px;width:450px">We have a choice of delivery options to ensure you receive your goods on time. Give us a call or email us to book a job. You can also visit your nearest Furnvale showroom.</p>
</section>

<h2 class="abs section-title" style="top:1143px">Our Products</h2>
<div class="abs product-photo" style="left:202px;background:linear-gradient(#c9c6c3,#9b9692)" role="img" aria-label="Grey framed glass sliding doors"></div>
<div class="abs product-photo" style="left:472px;background:linear-gradient(#6e5f50,#c5b7a3)" role="img" aria-label="Walk-in wardrobe system with hanging clothes"></div>
<div class="abs product-photo" style="left:742px;background:linear-gradient(90deg,#d9d9d7,#bfb6a9)" role="img" aria-label="White wardrobe storage shelves with baskets"></div>
<div class="abs product-name" style="left:202px">Sliding Doors</div>
<div class="abs product-name" style="left:472px">Wardrobe System</div>
<div class="abs product-name" style="left:742px">Storage Space</div>

<section class="abs process-band">
  <h2 class="abs section-title" style="top:36px">How does purchasing process work?</h2>
  <p class="abs lede" style="left:220px;top:74px;width:760px">We have a choice of delivery options to ensure you receive your goods on time. Give us a call or email us to book a job. You can also visit your nearest Furnvale showroom.</p>
  <div class="abs" style="left:208px;top:145px;width:360px">
    <div class="col-title" style="margin-bottom:12px">Lead Time</div>
    <div class="step"><svg width="17" height="17" viewBox="0 0 17 17"><circle cx="8.5" cy="8.5" r="7" fill="none" stroke="#fff" stroke-width="1.6"/><path d="M8.5 4.5v4.5l3 2" fill="none" stroke="#fff" stroke-width="1.6"/></svg>Normal lead time 2-3 weeks after placing order.</div>
    <div class="step"><svg width="17" height="17" viewBox="0 0 17 17"><circle cx="8.5" cy="8.5" r="7" fill="none" stroke="#fff" stroke-width="1.6"/><path d="M8.5 4.5v4.5l3 2" fill="none" stroke="#fff" stroke-width="1.6"/></svg>We do our own delivery and installation.</div>
    <div class="step"><svg width="17" height="17" viewBox="0 0 17 17"><circle cx="8.5" cy="8.5" r="7" fill="none" stroke="#fff" stroke-width="1.6"/><path d="M8.5 4.5v4.5l3 2" fill="none" stroke="#fff" stroke-width="1.6"/></svg>We do our own delivery and installation.</div>
  </div>
  <div class="abs" style="left:606px;top:145px;width:390px">
    <div class="col-title" style="margin-bottom:12px">Our Work Process</div>
    <div class="step"><svg width="18" height="18" viewBox="0 0 18 18"><path d="M2 16l1-4 9-9 3 3-9 9z" fill="#fff"/></svg>Come visit our showroom or we can meet you on site.</div>
    <div class="step"><svg width="18" height="18" viewBox="0 0 18 18"><path d="M2 16l1-4 9-9 3 3-9 9z" fill="#fff"/></svg>Design &amp; Quote.</div>
    <div class="step"><svg width="18" height="18" viewBox="0 0 18 18"><path d="M2 16l1-4 9-9 3 3-9 9z" fill="#fff"/></svg>Place your order.</div>
    <div class="step"><svg width="18" height="18" viewBox="0 0 18 18"><path d="M2 16l1-4 9-9 3 3-9 9z" fill="#fff"/></svg>Confirm delivery date with you (In 1-2 weeks after placing order).</div>
    <div class="step"><svg width="18" height="18" viewBox="0 0 18 18"><path d="M2 16l1-4 9-9 3 3-9 9z" fill="#fff"/></svg>Confirm installation date with you (In 1-2 weeks after delivery done).</div>
  </div>
</section>

<h2 class="abs section-title" style="top:1886px">Building Wardrobes</h2>
<p class="abs lede" style="left:210px;top:1925px;width:780px">We use cam-locks in our wood joinery. Our wardrobes can be disassembled with ease while offering the same stability as ordinary wardrobes built with screws/nails/dowels. We include a 5mm backboard in our wardrobe units for complete storage encasement.</p>

<div class="abs feature" style="left:204px;top:2016px">
  <svg width="34" height="34" viewBox="0 0 34 34"><rect x="9" y="3" width="16" height="28" rx="2" fill="#8a949c"/><g fill="#8a949c"><rect x="3" y="8" width="4" height="2"/><rect x="3" y="14" width="4" height="2"/><rect x="3" y="20" width="4" height="2"/><rect x="27" y="8" width="4" height="2"/><rect x="27" y="14" width="4" height="2"/><rect x="27" y="20" width="4" height="2"/></g></svg>
  <h3>Mechanisms and Fabrications</h3>
  <p>There is a wide range of mechanisms for your drawers and sliding doors. We supply Soft-Close sliding tracks for your drawers and Quiet-Slide tracking system for our sliding doors. If you need something different, please let us know.</p>
</div>
<div class="abs feature" style="left:469px;top:2016px">
  <svg width="34" height="34" viewBox="0 0 34 34"><rect x="9" y="3" width="16" height="28" rx="2" fill="#8a949c"/><g fill="#8a949c"><rect x="3" y="8" width="4" height="2"/><rect x="3" y="14" width="4" height="2"/><rect x="3" y="20" width="4" height="2"/><rect x="27" y="8" width="4" height="2"/><rect x="27" y="14" width="4" height="2"/><rect x="27" y="20" width="4" height="2"/></g></svg>
  <h3>Quality Control</h3>
  <p>We have international and local suppliers for a variety of components (glass, wood/melamine, PWC, and steel). We spend a lot of our time doing product, price, and quality comparisons. It is important to us to communicate these differences to you. Let us know what is important to you and we'll make it work. We can offer cost-effective and simple wardrobes or custom high-tech constructions.</p>
</div>
<div class="abs feature" style="left:735px;top:2016px">
  <svg width="34" height="34" viewBox="0 0 34 34"><rect x="9" y="3" width="16" height="28" rx="2" fill="#8a949c"/><g fill="#8a949c"><rect x="3" y="8" width="4" height="2"/><rect x="3" y="14" width="4" height="2"/><rect x="3" y="20" width="4" height="2"/><rect x="27" y="8" width="4" height="2"/><rect x="27" y="14" width="4" height="2"/><rect x="27" y="20" width="4" height="2"/></g></svg>
  <h3>Large Volume Supply</h3>
  <p>We are well-suited for commercial supply, we handle procurement/logistics/construction of wardrobes for apartment projects.</p>
</div>

<h2 class="abs section-title" style="top:2414px">Best Selling Products</h2>
<div class="abs" style="left:576px;top:2461px;width:48px;height:12px;border-radius:6px;background:#8cc63f" role="img" aria-label="Small green leaf divider"></div>

<div class="abs card" style="left:161px">
  <div class="card-photo" style="background:linear-gradient(#d8d6d2,#8a6a4e)" role="img" aria-label="Glass room divider in a bedroom"><span class="sale">Sale!</span></div>
  <div class="card-cat">Doors</div><div class="card-name">Room Divider</div>
  <div class="stars"><svg width="50" height="8" viewBox="0 0 50 8"><g fill="none" stroke="#7ab648" stroke-width=".8"><path d="M4 .5l1 2.4 2.6.2-2 1.7.6 2.6L4 6 1.8 7.4l.6-2.6-2-1.7 2.6-.2z"/><path transform="translate(10)" d="M4 .5l1 2.4 2.6.2-2 1.7.6 2.6L4 6 1.8 7.4l.6-2.6-2-1.7 2.6-.2z"/><path transform="translate(20)" d="M4 .5l1 2.4 2.6.2-2 1.7.6 2.6L4 6 1.8 7.4l.6-2.6-2-1.7 2.6-.2z"/><path transform="translate(30)" d="M4 .5l1 2.4 2.6.2-2 1.7.6 2.6L4 6 1.8 7.4l.6-2.6-2-1.7 2.6-.2z"/><path transform="translate(40)" d="M4 .5l1 2.4 2.6.2-2 1.7.6 2.6L4 6 1.8 7.4l.6-2.6-2-1.7 2.6-.2z"/></g></svg></div>
  <div class="price"><s>$555.00</s>$543.00</div>
</div>
<div class="abs card" style="left:384px">
  <div class="card-photo" style="background:linear-gradient(90deg,#e4e4e2,#f3f3f1)" role="img" aria-label="White hinged wardrobe doors"><span class="sale">Sale!</span></div>
  <div class="card-cat">Doors</div><div class="card-name">Hinge Doors</div>
  <div class="stars"><svg width="50" height="8" viewBox="0 0 50 8"><g fill="none" stroke="#7ab648" stroke-width=".8"><path d="M4 .5l1 2.4 2.6.2-2 1.7.6 2.6L4 6 1.8 7.4l.6-2.6-2-1.7 2.6-.2z"/><path transform="translate(10)" d="M4 .5l1 2.4 2.6.2-2 1.7.6 2.6L4 6 1.8 7.4l.6-2.6-2-1.7 2.6-.2z"/><path transform="translate(20)" d="M4 .5l1 2.4 2.6.2-2 1.7.6 2.6L4 6 1.8 7.4l.6-2.6-2-1.7 2.6-.2z"/><path transform="translate(30)" d="M4 .5l1 2.4 2.6.2-2 1.7.6 2.6L4 6 1.8 7.4l.6-2.6-2-1.7 2.6-.2z"/><path transform="translate(40)" d="M4 .5l1 2.4 2.6.2-2 1.7.6 2.6L4 6 1.8 7.4l.6-2.6-2-1.7 2.6-.2z"/></g></svg></div>
  <div class="price"><s>$789.00</s>$765.00</div>
</div>
<div class="abs card" style="left:607px">
  <div class="card-photo" style="background:linear-gradient(90deg,#c9c7c3,#9c9892,#d2c7b6)" role="img" aria-label="Bi-fold doors in grey and timber finish"><span class="sale">Sale!</span></div>
  <div class="card-cat">Bi-fold Doors</div><div class="card-name">Bi-fold Doors</div>
  <div class="stars"><svg width="50" height="8" viewBox="0 0 50 8"><g fill="none" stroke="#7ab648" stroke-width=".8"><path d="M4 .5l1 2.4 2.6.2-2 1.7.6 2.6L4 6 1.8 7.4l.6-2.6-2-1.7 2.6-.2z"/><path transform="translate(10)" d="M4 .5l1 2.4 2.6.2-2 1.7.6 2.6L4 6 1.8 7.4l.6-2.6-2-1.7 2.6-.2z"/><path transform="translate(20)" d="M4 .5l1 2.4 2.6.2-2 1.7.6 2.6L4 6 1.8 7.4l.6-2.6-2-1.7 2.6-.2z"/><path transform="translate(30)" d="M4 .5l1 2.4 2.6.2-2 1.7.6 2.6L4 6 1.8 7.4l.6-2.6-2-1.7 2.6-.2z"/><path transform="translate(40)" d="M4 .5l1 2.4 2.6.2-2 1.7.6 2.6L4 6 1.8 7.4l.6-2.6-2-1.7 2.6-.2z"/></g></svg></div>
  <div class="price"><s>$890.00</s>$765.00</div>
</div>
<div class="abs card" style="left:829px">
  <div class="card-photo" style="background:linear-gradient(#4b3f39,#2f2824)" role="img" aria-label="Dark melamine sliding doors"><span class="sale">Sale!</span></div>
  <div class="card-cat">Doors</div><div class="card-name">Melamine Sliding Doors</div>
  <div class="stars"><svg width="50" height="8" viewBox="0 0 50 8"><g fill="none" stroke="#7ab648" stroke-width=".8"><path d="M4 .5l1 2.4 2.6.2-2 1.7.6 2.6L4 6 1.8 7.4l.6-2.6-2-1.7 2.6-.2z"/><path transform="translate(10)" d="M4 .5l1 2.4 2.6.2-2 1.7.6 2.6L4 6 1.8 7.4l.6-2.6-2-1.7 2.6-.2z"/><path transform="translate(20)" d="M4 .5l1 2.4 2.6.2-2 1.7.6 2.6L4 6 1.8 7.4l.6-2.6-2-1.7 2.6-.2z"/><path transform="translate(30)" d="M4 .5l1 2.4 2.6.2-2 1.7.6 2.6L4 6 1.8 7.4l.6-2.6-2-1.7 2.6-.2z"/><path transform="translate(40)" d="M4 .5l1 2.4 2.6.2-2 1.7.6 2.6L4 6 1.8 7.4l.6-2.6-2-1.7 2.6-.2z"/></g></svg></div>
  <div class="price"><s>$800.00</s>$750.00</div>
</div>

<section class="abs suppliers">
  <h2 class="abs section-title" style="top:34px">Proudly Supplier</h2>
  <div class="abs badge" style="left:208px;top:80px">Harrow</div>
  <div class="abs badge" style="left:341px;top:80px">Panelcrest</div>
  <div class="abs badge" style="left:473px;top:80px">Keldane</div>
  <div class="abs badge" style="left:606px;top:80px">Marco Vellini</div>
  <div class="abs badge green" style="left:738px;top:80px">Brookfield</div>
  <div class="abs badge orange" style="left:871px;top:80px">Norvik</div>
  <div class="abs badge" style="left:208px;top:153px">Stonemere</div>
  <div class="abs badge" style="left:341px;top:153px">Formwright</div>
  <div class="abs badge" style="left:473px;top:153px">Lamisa</div>
  <div class="abs badge" style="left:606px;top:153px">Oakline</div>
  <div class="abs badge" style="left:738px;top:153px">Tessaro</div>
</section>

<section class="abs cta">
  <div class="abs cta-text" style="top:45px">Looking to renovate your wardrobe?</div>
  <div class="abs btn-shop" style="top:47px"><svg width="13" height="11" viewBox="0 0 13 11"><path d="M0 1h2.5l2 6.5h6.5l1.5-5H4" fill="none" stroke="#fff" stroke-width="1.5"/><circle cx="5.5" cy="9.8" r="1" fill="#fff"/><circle cx="10" cy="9.8" r="1" fill="#fff"/></svg>SHOP NOW</div>
</section>

<footer class="abs site-footer">
  <div class="abs brand" style="left:217px;top:138px"><span class="brand-square"></span>Furnvale</div>
  <div class="abs foot-head" style="left:398px;top:62px;width:200px;text-align:center">QUICK LINKS</div>
  <div class="abs foot-link active" style="left:398px;top:101px;width:200px;text-align:center">Home</div>
  <div class="abs" style="left:404px;top:121px;width:189px;height:2px;background:#555"></div>
  <div class="abs foot-link" style="left:398px;top:132px;width:200px;text-align:center">Products</div>
  <div class="abs foot-link" style="left:398px;top:163px;width:200px;text-align:center">Gallery</div>
  <div class="abs foot-link" style="left:398px;top:195px;width:200px;text-align:center">Buyer's Guide</div>

  <div class="abs foot-head" style="left:601px;top:62px;width:200px;text-align:center">PRODUCTS</div>
  <div class="abs foot-link" style="left:601px;top:101px;width:200px;text-align:center">Doors</div>
  <div class="abs foot-link" style="left:601px;top:132px;width:200px;text-align:center">Wardrobe System</div>
  <div class="abs foot-link" style="left:601px;top:163px;width:200px;text-align:center">Storage Space</div>
  <div class="abs foot-link" style="left:601px;top:195px;width:200px;text-align:center">Accessories</div>

  <div class="abs foot-head" style="left:847px;top:62px">OUR BRANCHES</div>
  <div class="abs branch" style="left:809px;top:93px">Auckland Showroom<br><span class="tel">09 555 0142</span><br>Hamilton Showroom<br><span class="tel">07 555 0187</span></div>
</footer>

</body>
</html>
```